Varnok Business Card

We are a security company in Central Aus, we supply guards, patrols, alarm monitoring, cash in transit, major event security.

I would like a modern card, possibly matte finish with gloss logo.... up for anything really

Our business colors are black white and blue.

on the back side of the card i was thinking having our logo just centered or our slogan ( "Securing Your Territory 24/7" )

Industry/Entity Type

Security

Contact Information for Business Card

Company Name: Varnok Security Service
My Name: Gregor Pellham
Position: Director
Mobil: 0491 738 205
Work: 89 612 347
Fax: 89 61 23 48
Email: greg.pellham@varnok-example.com.au
web: varnok-example.com.au
Address: 14 Quarry Road Alice Springs NT 0870

```html
<!DOCTYPE html>
<html lang="en">
<head>
<meta charset="utf-8">
<title>Varnok Security Service – Business Card</title>
<link rel="stylesheet" href="https://fonts.googleapis.com/css2?family=Cinzel:wght@400;600&display=swap">
<style>
  :root {
    --backdrop: #e6e8eb;
    --card: #ffffff;
    --brand-blue: #1b86c8;
    --wave-grey: #a7a9ac;
    --text-grey: #8a8c8f;
    --text-white: #ffffff;
  }
  * { box-sizing: border-box; margin: 0; padding: 0; }
  html, body {
    width: 1200px; height: 900px; overflow: hidden;
    background: var(--backdrop);
    font-family: "Cinzel", "Times New Roman", serif;
  }
  .canvas {
    position: relative; width: 1200px; height: 900px;
  }
  .card {
    position: absolute; left: 270px;
    width: 660px; height: 377px;
    background: var(--card);
    border-radius: 28px;
    overflow: hidden;
    box-shadow: 0 6px 18px rgba(0,0,0,0.12);
  }
  .card--back { top: 54px; }
  .card--front { top: 470px; }
  .card__wave { position: absolute; inset: 0; }

  .wordmark {
    position: absolute;
    color: var(--brand-blue);
    font-weight: 600;
    letter-spacing: 4px;
    text-transform: uppercase;
  }
  .card--back .wordmark {
    left: 0; right: 0; top: 150px;
    text-align: center; font-size: 56px;
  }
  .card--front .wordmark {
    right: 40px; top: 48px; font-size: 46px;
  }

  .holder {
    position: absolute; right: 70px; top: 220px;
    color: var(--text-grey); text-align: left;
    font-variant: small-caps;
  }
  .holder__name { font-size: 24px; letter-spacing: 1px; }
  .holder__role { font-size: 19px; letter-spacing: 2px; margin-top: 2px; }

  .contact {
    position: absolute; left: 22px; top: 148px;
    list-style: none; color: var(--text-white);
    font-size: 11.5px; line-height: 17px; letter-spacing: 0.3px;
  }
  .contact li { display: flex; align-items: flex-start; gap: 6px; }
  .contact svg { flex: none; margin-top: 2px; }
  .contact .wrap { max-width: 200px; }
</style>
</head>
<body>
<main class="canvas">

  <section class="card card--back" aria-label="Card back">
    <p class="wordmark">Varnok</p>
  </section>

  <section class="card card--front" aria-label="Card front">
    <svg class="card__wave" viewBox="0 0 660 377" aria-hidden="true">
      <path d="M0,28 C150,-10 250,40 300,150 C350,260 430,318 660,300 L660,377 L0,377 Z" fill="var(--wave-grey)"/>
      <path d="M0,46 C140,10 236,60 284,166 C336,276 420,336 660,322 L660,377 L0,377 Z" fill="var(--card)"/>
      <path d="M0,58 C130,26 222,74 268,178 C320,290 410,350 660,338 L660,377 L0,377 Z" fill="var(--brand-blue)"/>
    </svg>

    <p class="wordmark">Varnok</p>

    <div class="holder">
      <p class="holder__name">Gregor Pellham</p>
      <p class="holder__role">Director</p>
    </div>

    <ul class="contact">
      <li>
        <svg width="10" height="10" viewBox="0 0 10 10"><circle cx="5" cy="5" r="5" fill="#fff"/><path d="M5 2a2 2 0 0 1 2 2c0 1.5-2 4-2 4S3 5.5 3 4a2 2 0 0 1 2-2z" fill="var(--brand-blue)"/></svg>
        <span class="wrap">14 Quarry Road Alice Springs NT 0870</span>
      </li>
      <li>
        <svg width="10" height="10" viewBox="0 0 10 10"><circle cx="5" cy="5" r="5" fill="#fff"/><rect x="3.5" y="2" width="3" height="6" rx="0.6" fill="var(--brand-blue)"/></svg>
        <span>0491 738 205</span>
      </li>
      <li>
        <svg width="10" height="10" viewBox="0 0 10 10"><circle cx="5" cy="5" r="5" fill="#fff"/><path d="M3 3.2c.5-.6 1-.6 1.3 0l.4.9-.6.5c.3.7.8 1.2 1.3 1.4l.5-.6.9.4c.6.3.6.8 0 1.3C5 8 2 5 3 3.2z" fill="var(--brand-blue)"/></svg>
        <span>89 612 347</span>
      </li>
      <li>
        <svg width="10" height="10" viewBox="0 0 10 10"><circle cx="5" cy="5" r="5" fill="#fff"/><rect x="2.5" y="4" width="5" height="3" fill="var(--brand-blue)"/><rect x="3.5" y="2.5" width="3" height="1.5" fill="var(--brand-blue)"/></svg>
        <span>89 61 23 48</span>
      </li>
      <li>
        <svg width="10" height="10" viewBox="0 0 10 10"><circle cx="5" cy="5" r="5" fill="#fff"/><rect x="2.5" y="3.2" width="5" height="3.6" fill="var(--brand-blue)"/><path d="M2.5 3.2L5 5.3l2.5-2.1" stroke="#fff" stroke-width="0.6" fill="none"/></svg>
        <span>greg.pellham@varnok-example.com.au</span>
      </li>
      <li>
        <svg width="10" height="10" viewBox="0 0 10 10"><circle cx="5" cy="5" r="5" fill="#fff"/><circle cx="5" cy="5" r="2.6" fill="none" stroke="var(--brand-blue)" stroke-width="0.7"/><path d="M2.4 5h5.2M5 2.4v5.2" stroke="var(--brand-blue)" stroke-width="0.6"/></svg>
        <span>www.varnok-example.com.au</span>
      </li>
    </ul>
  </section>

</main>
</body>
</html>
```